LarkTips.net Redesign - PSD Home Page + 2 Templates

Need a new template style for 3 web page designs (layout and graphics only) for LarkTips.net. Pages will have the same look and feel but serve different purposes so there may be some differences. Contest winner will not be required to do the HTML or CSS.
I need 1 style/template applied to the following 3 page designs as part of this project:
1. Home page
2. Template for Weekly Picks Page
3. Template for Overview Page (Landing Page)
I will not want to stray too far from existing look at feel (colors, some graphics, clean look, etc...) but will entertain any design suggestions. So don''''t hesitate to get creative!
I will not want to stray too far from existing look at feel (colors,
some graphics, clean look, etc...) but will entertain any design
suggestions. So don''''t hesitate to get creative!
Home Page
This page can take some liberties with flash (optional, although NOT
entirely flash) and will remain mainly static. It should be a quick
and easy starting point to get users to the rest of the site. Clean
and simple.
Overview Pages - Landing pages - for example they will replace these types of pages:
http://www.larktips.net/pro-tips.php
http://www.larktips.net/free-diamond-tips.php
http://www.larktips.net/campus-gridiron-tips.php
http://www.larktips.net/aboutus.htm
http://www.larktips.net/free-gridiron-tips.php
Weekly Picks Pages
These are the pages where picks get posted each week.
Designs requiring tables will NOT be accepted - must allow for coding to use SEO friendly design/CSS to create.
For example:
http://www.larktips.net/gridiron/2008-Pro-Tips/week11.php
and
http://www.larktips.net/campus-gridiron-tips/2008/week13.php
These pages will need to have a SHARE button on the page, for example
the PassAlong.io Share button or similiar. Somewhere within the
navigation design/navigation.
Because I know many designers ask here are some website designs I like
(without the ads), feel free to use these or actually have an original
thought. I am open to any design so don''''t let these over influence you!
Mystvale77.com
GratisGridironHunches.net
brennowagers.com
pellworth-hollows.com
learnvista.org/
Target Market(s)
Men - Age 18 - 75
Sports Fan
Gamblers
Large Existing Client Base
Requirements
Must have
- Clean Design
- Easy, Clear Navigation
Nice to have
- See project brief
Should not have
- Anything that will need tables when HTML is created.

```html
<!DOCTYPE html>
<html lang="en">
<head>
<meta charset="utf-8">
<title>LarkTips.net – Home</title>
<link rel="stylesheet" href="https://fonts.googleapis.com/css2?family=Montserrat:wght@800;900&family=Handlee&family=Arimo:wght@400&display=swap">
<style>
  :root{
    --lime:#d9f200;
    --lime-deep:#8fdc00;
    --ink:#1a1a1a;
    --paper:#ffffff;
    --photo-dark:#2b1a18;
    --photo-mid:#7a3a32;
    --photo-light:#c98a7a;
  }
  *{margin:0;padding:0;box-sizing:border-box}
  html,body{width:832px;height:1200px;overflow:hidden;background:var(--paper)}
  .page{position:relative;width:832px;height:1200px;color:var(--ink);font-family:"Arimo",Arial,sans-serif}
  .abs{position:absolute}
  .brand{left:0;width:832px;top:42px;text-align:center;font-family:"Montserrat",sans-serif;font-weight:900;font-size:60px;letter-spacing:-2px;color:var(--ink)}
  .nav{left:0;top:150px;width:832px;height:170px}
  .nav-label{top:290px;width:150px;text-align:center;font-family:"Handlee",cursive;font-size:22px;color:#222}
  .hero{left:19px;top:341px;width:791px;height:285px;background:var(--lime);border-radius:24px}
  .hero-title{left:46px;top:365px;width:290px;font-family:"Montserrat",sans-serif;font-weight:900;font-size:24px;line-height:35px;white-space:nowrap;letter-spacing:-0.3px}
  .hero-title span{display:block}
  .hero-copy{left:49px;top:454px;width:272px;font-family:"Handlee",cursive;font-size:20px;line-height:27.5px}
  .hero-copy span{display:block;text-align:justify;text-align-last:justify;white-space:nowrap}
  .hero-copy .spread{letter-spacing:27px;margin-right:-27px}
  .hero-copy .spread-url{letter-spacing:10px;margin-right:-10px}
  .hero-frame{left:368px;top:368px;width:417px;height:235px;background:#0d0d0d;border-radius:10px}
  .hero-photo{left:394px;top:396px;width:380px;height:179px;background:linear-gradient(180deg,var(--photo-light) 0%,var(--photo-mid) 45%,var(--photo-dark) 100%)}
  .section-title{font-family:"Handlee",cursive;font-size:26px;color:#222}
  .rule{height:5px;background:var(--lime)}
  .copy{font-size:10.5px;line-height:13.8px;color:#111}
  .register{left:436px;top:659px;width:365px;height:124px;border-radius:6px;background:linear-gradient(180deg,var(--lime) 0%,var(--lime-deep) 100%)}
  .register-title{left:457px;top:675px;font-family:"Montserrat",sans-serif;font-weight:900;font-size:22px;letter-spacing:-0.5px}
  .register-copy{left:457px;top:705px;width:230px;font-family:"Handlee",cursive;font-size:20px;line-height:29px}
  .footer{left:20px;top:1029px;width:792px;height:135px;background:var(--lime);border-radius:22px}
  .footer-head{top:1048px;font-family:"Handlee",cursive;font-size:20px}
  .footer-links{top:1078px;list-style:none;font-size:8.6px;line-height:11px}
  .disclaimer{left:365px;top:1046px;width:420px;font-family:"Handlee",cursive;font-size:20.5px;line-height:27px;text-align:justify;letter-spacing:0.5px}
</style>
</head>
<body>
<div class="page">

  <div class="abs brand">LarkTips.net</div>

  <svg class="abs nav" viewBox="0 150 832 170" aria-label="Sport navigation">
    <rect x="110" y="218" width="610" height="10" fill="var(--lime)"/>
    <g fill="var(--paper)" stroke="var(--lime)" stroke-width="12">
      <circle cx="111" cy="223" r="54"/>
      <circle cx="261" cy="223" r="54"/>
      <circle cx="413" cy="223" r="54"/>
      <circle cx="563" cy="223" r="54"/>
      <circle cx="717" cy="223" r="54"/>
    </g>
    <ellipse cx="111" cy="223" rx="33" ry="19" fill="var(--ink)"/>
    <g stroke="var(--paper)" stroke-width="2">
      <line x1="94" y1="223" x2="128" y2="223"/>
      <line x1="100" y1="218" x2="100" y2="228"/><line x1="106" y1="218" x2="106" y2="228"/>
      <line x1="112" y1="218" x2="112" y2="228"/><line x1="118" y1="218" x2="118" y2="228"/>
      <line x1="124" y1="218" x2="124" y2="228"/>
    </g>
    <path d="M228 202 L240 200 L253 234 L296 234 L296 248 L248 248 Q240 248 238 240 Z" fill="var(--ink)"/>
    <ellipse cx="282" cy="216" rx="15" ry="7" fill="var(--ink)"/>
    <rect x="267" y="216" width="30" height="9" fill="var(--ink)"/>
    <text x="413" y="246" text-anchor="middle" font-family="Montserrat, sans-serif" font-weight="800" font-size="64" fill="var(--ink)">H</text>
    <circle cx="563" cy="223" r="35" fill="var(--ink)"/>
    <g fill="none" stroke="var(--paper)" stroke-width="2.5">
      <line x1="528" y1="223" x2="598" y2="223"/>
      <line x1="563" y1="188" x2="563" y2="258"/>
      <path d="M540 196 Q556 223 540 250"/>
      <path d="M586 196 Q570 223 586 250"/>
    </g>
    <circle cx="717" cy="223" r="36" fill="var(--ink)"/>
    <g fill="none" stroke="var(--paper)" stroke-width="2.5" stroke-dasharray="3 3">
      <path d="M700 192 Q716 223 700 254"/>
      <path d="M734 192 Q718 223 734 254"/>
    </g>
  </svg>
  <div class="abs nav-label" style="left:36px">Football</div>
  <div class="abs nav-label" style="left:186px;top:294px">Hockey</div>
  <div class="abs nav-label" style="left:338px;top:293px">Home</div>
  <div class="abs nav-label" style="left:474px;top:293px">Basketball</div>
  <div class="abs nav-label" style="left:630px">Baseball</div>

  <section class="abs hero"></section>
  <h1 class="abs hero-title"><span>Free online sports</span><span>picks and tips ...</span></h1>
  <p class="abs hero-copy">
    <span>Get Lark's picks on PGL,</span>
    <span>PBL, PHL, CAA and</span>
    <span class="spread">baseball</span>
    <span>games. Bet smarter with</span>
    <span class="spread-url">LarkTips.net!</span>
  </p>
  <div class="abs hero-frame"></div>
  <div class="abs hero-photo" role="img" aria-label="Photo of two fans seen from behind watching a game in a packed arena"></div>

  <h2 class="abs section-title" style="left:35px;top:660px">Weekly PGL Picks</h2>
  <div class="abs rule" style="left:28px;top:700px;width:358px"></div>
  <p class="abs copy" style="left:35px;top:722px;width:350px">Week 1 PGL Tips, Week 2 PGL Tips, Week 3 Tips, Week 4 PGL Tips Lorem Ipsum Lorem Ipsum Lorem Ipsum Lorem Ipsum Lorem Ipsum Lorem Ipsum Lorem Ipsum Lorem Ipsum Lorem Ipsum Lorem Ipsum Lorem Ipsum Lorem Ipsum Lorem Ipsum Lorem Ipsum Lorem Ipsum Lorem Ipsum Lorem Ipsum Lorem Ipsum Lorem Ipsum Lorem Ipsum Lorem Ipsum Lorem Ipsum Lorem Ipsum Lorem Ipsum Lorem Ipsum</p>

  <h2 class="abs section-title" style="left:33px;top:836px">Weekly PBL Picks</h2>
  <div class="abs rule" style="left:28px;top:877px;width:358px"></div>
  <p class="abs copy" style="left:33px;top:898px;width:350px">Week 1 PGL Tips, Week 2 PGL Tips, Week 3 Tips, Week 4 PGL Tips Lorem Ipsum Lorem Ipsum Lorem Ipsum Lorem Ipsum Lorem Ipsum Lorem Ipsum Lorem Ipsum Lorem Ipsum Lorem Ipsum Lorem Ipsum Lorem Ipsum Lorem Ipsum Lorem Ipsum Lorem Ipsum Lorem Ipsum Lorem Ipsum Lorem Ipsum Lorem Ipsum Lorem Ipsum Lorem Ipsum Lorem Ipsum Lorem Ipsum Lorem Ipsum Lorem Ipsum Lorem Ipsum</p>

  <div class="abs register"></div>
  <div class="abs register-title">REGISTER NOW!</div>
  <p class="abs register-copy">Get email updates + exclusive free picks ...</p>
  <svg class="abs" style="left:695px;top:684px" width="90" height="73" viewBox="0 0 90 73" aria-label="Email icon">
    <rect x="2" y="2" width="86" height="69" fill="none" stroke="var(--ink)" stroke-width="4"/>
    <rect x="64" y="8" width="18" height="15" fill="var(--ink)"/>
    <rect x="18" y="30" width="40" height="6" fill="var(--ink)"/>
    <rect x="26" y="41" width="34" height="6" fill="var(--ink)"/>
    <rect x="26" y="52" width="34" height="6" fill="var(--ink)"/>
  </svg>

  <h2 class="abs section-title" style="left:429px;top:817px">Latest Lark's Pick Blog</h2>
  <div class="abs rule" style="left:426px;top:858px;width:352px"></div>
  <p class="abs copy" style="left:427px;top:879px;width:350px">Lorem Ipsum Lorem Ipsum Lorem Ipsum Lorem Ipsum Lorem Ipsum Lorem Ipsum Lorem Ipsum Lorem Ipsum Lorem Ipsum Lorem Ipsum Lorem Ipsum Lorem Ipsum Lorem Ipsum Lorem Ipsum Lorem Ipsum Lorem Ipsum Lorem Ipsum Lorem Ipsum Lorem Ipsum Lorem Ipsum Lorem Ipsum Lorem Ipsum Lorem Ipsum Lorem Ipsum Lorem Ipsum</p>

  <footer class="abs footer"></footer>
  <div class="abs footer-head" style="left:43px">Picks</div>
  <ul class="abs footer-links" style="left:43px">
    <li>Football Picks</li><li>Basketball Picks</li><li>Hockey Picks</li><li>Baseball Picks</li><li>Free Picks</li>
  </ul>
  <div class="abs footer-head" style="left:143px">About</div>
  <ul class="abs footer-links" style="left:143px;top:1080px">
    <li>Home</li><li>Conact us</li><li>Site map</li><li>Privacy Policy</li>
  </ul>
  <div class="abs footer-head" style="left:242px">Other</div>
  <ul class="abs footer-links" style="left:242px;top:1079px">
    <li>Monday Night Picks</li><li>Handicapping Links</li><li>Fantasy Football</li>
  </ul>
  <p class="abs disclaimer">This website is for entertainment purposes only. I do not condone or encourage any type of illegal wagering.</p>

</div>
</body>
</html>
```